Construction training company needs a workshop invitation template

We need an invitation template for our professional development workshops we run for construction companies.
We would like to see designs that use the colors in our Framehold Sentinel Logo.
A simple, clean design with a lot of white space would be preferred.
No reverse text or italics.
The template should be done in Adobe Illustrator.

• Reverse text or italics

```html
<!DOCTYPE html>
<html lang="en">
<head>
<meta charset="utf-8">
<title>Framehold Sentinel Workshop Invitation</title>
<link href="https://fonts.googleapis.com/css2?family=Arimo:wght@400;700&family=Libre+Baskerville:wght@700&family=Tinos:wght@400&display=swap" rel="stylesheet">
<style>
  :root{
    --bg:#ececea;
    --paper:#fbfbfa;
    --green:#7cbb2e;
    --green-dark:#4f9a2a;
    --green-light:#a8d845;
    --ink:#3b3b3b;
    --ink-soft:#5a5a5a;
    --rule:#cfcfcf;
    --plan:#e2e2e2;
  }
  *{box-sizing:border-box;margin:0;padding:0}
  html,body{width:1200px;height:900px;overflow:hidden}
  body{background:var(--bg);font-family:"Arimo",Arial,sans-serif;color:var(--ink);
    display:flex;align-items:center;justify-content:center;gap:40px}
  .card{position:relative;width:560px;height:396px;background:var(--paper);
    box-shadow:0 6px 18px rgba(0,0,0,.14);overflow:hidden}
  .plan-art{position:absolute;left:0;bottom:0;width:190px;height:150px;
    background:linear-gradient(45deg,var(--plan),rgba(240,240,240,0) 75%)}
  .brand{display:flex;align-items:center;gap:8px}
  .brand-mark{width:26px;height:26px;border-radius:50%;background:var(--green)}
  .brand-name{font-size:14px;font-weight:700;letter-spacing:1.5px;text-transform:uppercase;color:var(--ink);line-height:1.15}
  .brand-sub{font-size:10px;color:var(--ink-soft);letter-spacing:.3px}
  .pill{display:inline-block;background:linear-gradient(90deg,var(--green-dark),var(--green-light));
    color:#fff;border-radius:14px;font-size:14px;padding:6px 26px;box-shadow:0 3px 5px rgba(0,0,0,.2)}

  /* front */
  .front{text-align:center}
  .front .brand{position:absolute;left:150px;top:44px}
  .invite-title{position:absolute;top:108px;left:0;right:0;font-family:"Libre Baskerville",Georgia,serif;
    font-size:40px;color:var(--green);letter-spacing:1px}
  .invite-lead{position:absolute;top:172px;left:0;right:0;font-size:13px;color:var(--ink-soft)}
  .invite-event{position:absolute;top:192px;left:0;right:0;font-size:16px;font-weight:700;color:var(--ink)}
  .front .pill{position:absolute;top:222px;left:50%;transform:translateX(-50%);white-space:nowrap}
  .invite-venue{position:absolute;top:268px;left:0;right:0;font-size:14px;color:var(--ink-soft)}
  .invite-notes{position:absolute;top:296px;left:0;right:0;font-size:11px;line-height:1.55;color:var(--ink-soft)}
  .invite-more{position:absolute;top:352px;left:0;right:0;font-size:8px;color:var(--ink-soft)}

  /* back */
  .back .brand{position:absolute;left:50%;top:24px;transform:translateX(-50%)}
  .back-heading{position:absolute;top:76px;left:0;right:0;text-align:center;font-size:13px;color:var(--ink)}
  .topics{position:absolute;top:100px;left:34px;right:34px;display:flex;gap:24px}
  .topic-list{flex:1;list-style:none;font-family:"Tinos","Times New Roman",serif;font-size:10.5px;color:var(--ink-soft)}
  .topic-list li{position:relative;padding:4px 0 4px 12px;border-top:1px dotted var(--rule);line-height:1.2}
  .topic-list li::before{content:"";position:absolute;left:1px;top:7px;width:6px;height:6px;border-radius:50%;background:var(--green)}
  .back .pill{position:absolute;top:318px;left:50%;transform:translateX(-50%);white-space:nowrap;font-size:13px}
  .back-venue{position:absolute;top:358px;left:0;right:0;text-align:center;font-size:10px;color:var(--ink-soft)}
</style>
</head>
<body>

<section class="card front">
  <div class="plan-art" role="img" aria-label="Faint architectural floor plan and building sketch"></div>
  <div class="brand">
    <span class="brand-mark"></span>
    <div>
      <div class="brand-name">Framehold<br>Sentinel</div>
      <div class="brand-sub">Professional Development</div>
    </div>
  </div>
  <h1 class="invite-title">YOU’RE INVITED!</h1>
  <p class="invite-lead">Brackwell Builders invite you to a</p>
  <p class="invite-event">Framehold Sentinel Professional Development Workshop</p>
  <span class="pill">Wednesday the 7th of June 2021</span>
  <p class="invite-venue">At [address of venue inserted here] 7:00 AM to 12 noon</p>
  <p class="invite-notes">The case study at this workshop will be the Brackwell Builders<br>project at 14 Tallow St, Ferncliff<br>And there’s no charge for attending!</p>
  <p class="invite-more">See reverse side for more info...</p>
</section>

<section class="card back">
  <div class="plan-art" role="img" aria-label="Faint architectural floor plan sketch"></div>
  <div class="brand">
    <span class="brand-mark"></span>
    <div>
      <div class="brand-name">Framehold<br>Sentinel</div>
      <div class="brand-sub">Professional Development</div>
    </div>
  </div>
  <p class="back-heading">This is a live action workshop where you participate in and learn about...</p>
  <div class="topics">
    <ul class="topic-list">
      <li>How to set up a smart schedule for a construction project</li>
      <li>How to get clarity on the building work to be done, using a 3D model</li>
      <li>Getting everybody onto the same page</li>
      <li>Solving construction headaches before they happen</li>
      <li>Getting the information you need to make you more efficient and effective</li>
      <li>How to get more satisfaction out of your work</li>
      <li>Delivering projects in less time and at lower costs</li>
      <li>Achieving better quality work</li>
    </ul>
    <ul class="topic-list">
      <li>Ensuring a high level of worksite safety</li>
      <li>Developing stronger relationships within the workforce</li>
      <li>How smart collaboration can improve things for everybody</li>
      <li>Transforming workplace culture and reducing the mental health issues in the construction industry</li>
      <li>Reducing rework and warranty work</li>
      <li>Creating better results, with less time, effort and cost</li>
      <li>Boosting customer satisfaction and referrals</li>
    </ul>
  </div>
  <span class="pill">Seats are limited, so book your spot today! Call Marnie on 0400 555 019</span>
  <p class="back-venue">At [address of venue inserted here] 7:00 AM to 12 noon</p>
</section>

</body>
</html>
```